Tradeora Banner Design for B2B Consulting Firm

Take the already developed logo (attached) and incorporate it into a creative banner design for placement on Tradeora (the social media platform targeting business users). The banner will be used on the firm's company profile page on Tradeora (not yet created).

```html
<!DOCTYPE html>
<html lang="en">
<head>
<meta charset="utf-8">
<title>Alderpath — Tradeora Company Banner</title>
<link rel="stylesheet" href="https://fonts.googleapis.com/css2?family=Source+Sans+3:wght@400;700&display=swap">
<style>
  :root {
    --backdrop: #c0c0c0;
    --forest: #466349;
    --paper: #ffffff;
  }
  * { margin: 0; padding: 0; box-sizing: border-box; }
  html, body {
    width: 1200px;
    height: 492px;
    overflow: hidden;
    background: var(--backdrop);
    font-family: "Source Sans 3", "Myriad Pro", Arial, sans-serif;
  }
  .stage {
    position: relative;
    width: 1200px;
    height: 492px;
  }
  .banner {
    position: absolute;
    left: 72px;
    top: 157px;
    width: 1057px;
    height: 178px;
    background: var(--forest);
    overflow: hidden;
  }
  .banner__waves {
    position: absolute;
    inset: 0;
    width: 100%;
    height: 100%;
  }
  .banner__wave { fill: var(--paper); }
  .banner__copy {
    position: absolute;
    left: 387px;
    top: 50px;
    color: var(--paper);
  }
  .banner__headline {
    font-weight: 700;
    font-size: 23px;
    line-height: 27px;
    letter-spacing: -0.1px;
  }
  .banner__audience {
    margin-top: 18px;
    font-weight: 400;
    font-size: 11.6px;
    line-height: 14px;
    white-space: nowrap;
  }
  .banner__brand {
    position: absolute;
    left: 948px;
    top: 118px;
    transform: translate(-50%, -50%);
    color: var(--paper);
    font-weight: 700;
    font-size: 13px;
    letter-spacing: 0.3px;
  }
</style>
</head>
<body>
  <main class="stage">
    <section class="banner" aria-label="Alderpath company banner">
      <svg class="banner__waves" viewBox="0 0 1374 232" preserveAspectRatio="none" aria-hidden="true">
        <path class="banner__wave" d="M0,43 C30,45 45,80 62,112 C82,150 112,160 190,165 C258,170 284,192 300,232 L0,232 Z"/>
        <path class="banner__wave" d="M1047,0 C1062,40 1112,62 1200,66 C1280,70 1302,92 1320,132 C1340,176 1354,187 1374,187 L1374,0 Z"/>
      </svg>
      <div class="banner__copy">
        <h1 class="banner__headline">Providing Fractional&nbsp; Marketing<br>Services to B2B clients</h1>
        <p class="banner__audience">such as Private Equity Firms, Family Offices, Investment Banks, and Independent Sponsors</p>
      </div>
      <span class="banner__brand">Alderpath</span>
    </section>
  </main>
</body>
</html>
```